Criação de Papelaria Profissional para Vértice & Prisma
A empresa queria:
" Desenvolve, vende, implanta o Software e da suporte (Atendimento ao cliente). "

```html
<!DOCTYPE html>
<html lang="pt-BR">
<head>
<meta charset="utf-8">
<title>Vértice &amp; Prisma — Papel Timbrado</title>
<link href="https://fonts.googleapis.com/css2?family=Open+Sans:wght@400;600;700&display=swap" rel="stylesheet">
<style>
  :root {
    --backdrop: #d9d9d9;
    --paper: #ffffff;
    --brand-orange: #f08a1c;
    --ink-dark: #2b2b2b;
    --ink-body: #6b6b6b;
    --ink-soft: #8a8a8a;
  }
  * { box-sizing: border-box; margin: 0; padding: 0; }
  html, body {
    width: 1200px; height: 1200px; overflow: hidden;
    background: var(--backdrop);
    font-family: "Open Sans", Arial, sans-serif;
  }
  .letterhead {
    position: absolute; left: 211px; top: 50px;
    width: 778px; height: 1100px;
    background: var(--paper);
    box-shadow: 0 4px 18px rgba(0,0,0,0.12);
  }
  .brand {
    position: absolute; top: 58px; right: 64px;
    display: flex; align-items: center; gap: 12px;
  }
  .brand-dot {
    width: 40px; height: 40px; border-radius: 50%;
    background: var(--brand-orange);
  }
  .brand-text { display: flex; flex-direction: column; align-items: flex-end; }
  .brand-name {
    font-weight: 700; font-size: 30px; line-height: 1;
    color: var(--ink-dark); letter-spacing: -0.5px;
  }
  .brand-tagline {
    font-size: 11px; color: var(--brand-orange);
    letter-spacing: 4px; text-transform: lowercase; margin-top: 4px;
  }
  .letter-body {
    position: absolute; top: 190px; left: 72px; right: 72px;
    font-size: 13px; line-height: 1.75; color: var(--ink-body);
    text-align: justify;
  }
  .letter-body p + p { margin-top: 16px; }
  .contact-bar {
    position: absolute; left: 72px; right: 72px; bottom: 52px;
    display: flex; gap: 48px;
    font-size: 11px; line-height: 1.5; color: var(--ink-soft);
  }
  .contact-item { display: flex; align-items: flex-start; gap: 8px; }
  .contact-icon { width: 18px; height: 18px; flex: none; }
  .bottom-band {
    position: absolute; left: 0; right: 0; bottom: 0; height: 16px;
    background: var(--brand-orange);
  }
</style>
</head>
<body>
  <main class="letterhead">
    <header class="brand">
      <span class="brand-dot"></span>
      <div class="brand-text">
        <span class="brand-name">Vértice &amp; Prisma</span>
        <span class="brand-tagline">software</span>
      </div>
    </header>

    <section class="letter-body">
      <p>Prezado cliente, apresentamos nossa nova linha de soluções em software para gestão empresarial. Nossa equipe desenvolve, vende e implanta sistemas sob medida, sempre com foco em qualidade, agilidade e segurança das informações da sua empresa.</p>
      <p>Oferecemos também suporte técnico dedicado e atendimento ao cliente em todas as etapas do projeto, desde o primeiro contato até o acompanhamento após a implantação. Cada solução é planejada para atender às necessidades reais do seu negócio e crescer junto com ele.</p>
      <p>Agradecemos a confiança e permanecemos à disposição para esclarecer dúvidas e agendar uma demonstração.</p>
    </section>

    <footer class="contact-bar">
      <div class="contact-item">
        <svg class="contact-icon" viewBox="0 0 18 18" aria-hidden="true">
          <circle cx="9" cy="9" r="9" fill="var(--brand-orange)"/>
          <path d="M6 4.5c.6 0 1.6 2 1.4 2.4l-.8.9c.5 1.2 1.4 2.1 2.6 2.6l.9-.8c.4-.2 2.4.8 2.4 1.4 0 .8-1 1.8-1.8 1.6C7.8 12 6 10.2 5.4 7.3 5.2 6.5 5.2 4.5 6 4.5z" fill="#fff"/>
        </svg>
        <span>(19) 4000-1234<br>(19) 99000-5678</span>
      </div>
      <div class="contact-item">
        <svg class="contact-icon" viewBox="0 0 18 18" aria-hidden="true">
          <circle cx="9" cy="9" r="9" fill="var(--brand-orange)"/>
          <rect x="4.5" y="5.8" width="9" height="6.4" rx="0.8" fill="none" stroke="#fff" stroke-width="1.2"/>
          <path d="M4.8 6.2 9 9.4l4.2-3.2" fill="none" stroke="#fff" stroke-width="1.2"/>
        </svg>
        <span>www.verticeprisma.com.br<br>contato@verticeprisma.com.br</span>
      </div>
      <div class="contact-item">
        <svg class="contact-icon" viewBox="0 0 18 18" aria-hidden="true">
          <circle cx="9" cy="9" r="9" fill="var(--brand-orange)"/>
          <path d="M9 4a3.2 3.2 0 0 1 3.2 3.2C12.2 9.6 9 14 9 14S5.8 9.6 5.8 7.2A3.2 3.2 0 0 1 9 4z" fill="#fff"/>
          <circle cx="9" cy="7.2" r="1.2" fill="var(--brand-orange)"/>
        </svg>
        <span>Rua das Acácias, 120<br>Campinas - SP, CEP 13010-000</span>
      </div>
    </footer>

    <div class="bottom-band"></div>
  </main>
</body>
</html>
```